Silver Brook Constructions Ltd Stationary
business cards, stationary etc.
Silver Brook Constructions Ltd Stationary - Construction
Creative Brief
Simple
Dalton Wexford
4816 Ardmore Rd. Victoria B.C. V8N 4K7
250-384-6252 could we put this number under office instead of phone
222-222-2222 temporary until I get new number
dalton@silverbrookconstructions.example
www.silverbrookconstructions.example
We would like designs for business cards , envelopes, letterhead, thank-you cards with evelopes, fax cover sheet, and presentation folder. Thank you
information should be on the back of the card along with some clean lines and simplicity while keeping a very professional feel

```html
<!DOCTYPE html>
<html lang="en">
<head>
<meta charset="utf-8">
<title>Silver Brook Constructions Ltd Stationary – Business Cards</title>
<link rel="stylesheet" href="https://fonts.googleapis.com/css2?family=Cinzel:wght@400;600&family=Crimson+Text:wght@400&display=swap">
<style>
  :root {
    --page-bg: #e9e6e1;
    --card-white: #ffffff;
    --ink-black: #141414;
    --brand-green: #6b8a34;
    --text-grey: #6a6a6a;
    --rule-grey: #c9c9c9;
  }
  * { margin: 0; padding: 0; box-sizing: border-box; }
  html, body { width: 1200px; height: 852px; overflow: hidden; }
  body { background: var(--page-bg); position: relative; font-family: "Crimson Text", Georgia, serif; }

  .card {
    position: absolute;
    width: 540px; height: 309px;
    background: var(--card-white);
    border-radius: 18px;
    overflow: hidden;
    box-shadow: 0 8px 24px rgba(0,0,0,0.18);
  }
  .card--back { left: 50px; top: 90px; }
  .card--front { left: 610px; top: 453px; }
  .card__edges { position: absolute; inset: 0; width: 100%; height: 100%; }

  /* back */
  .holder-name {
    position: absolute; left: 140px; top: 52px;
    font-family: "Cinzel", "Times New Roman", serif; font-weight: 400;
    font-size: 27px; color: var(--brand-green); letter-spacing: 0.5px;
  }
  .address {
    position: absolute; right: 310px; top: 158px;
    text-align: right; font-size: 15px; line-height: 1.3; color: var(--text-grey);
  }
  .divider {
    position: absolute; left: 245px; top: 150px;
    width: 1px; height: 108px; background: var(--rule-grey);
  }
  .contacts { position: absolute; left: 255px; top: 146px; list-style: none; }
  .contacts li {
    display: flex; align-items: center; gap: 7px;
    font-size: 13px; line-height: 27px; color: var(--text-grey); white-space: nowrap;
  }
  .contacts svg { width: 14px; height: 14px; flex: none; }

  /* front */
  .brand {
    position: absolute; left: 0; right: 0; top: 78px;
    display: flex; flex-direction: column; align-items: center;
  }
  .brand__dot {
    width: 62px; height: 62px; border-radius: 50%;
    background: var(--brand-green); margin-bottom: 16px;
  }
  .brand__name {
    font-family: "Cinzel", "Times New Roman", serif; font-weight: 600;
    font-size: 26px; line-height: 1.25; color: var(--ink-black);
    text-align: center; letter-spacing: 1px;
  }
</style>
</head>
<body>

<section class="card card--back" aria-label="Business card back">
  <svg class="card__edges" viewBox="0 0 540 309" aria-hidden="true">
    <path d="M0,0 H70 C35,70 14,170 0,260 Z" fill="var(--ink-black)"/>
    <path d="M88,-4 C48,70 22,170 12,315" fill="none" stroke="var(--brand-green)" stroke-width="7"/>
    <path d="M540,170 C528,240 490,290 430,309 H540 Z" fill="var(--ink-black)"/>
    <path d="M534,150 C522,235 480,290 410,315" fill="none" stroke="var(--brand-green)" stroke-width="7"/>
  </svg>
  <h1 class="holder-name">Dalton Wexford</h1>
  <p class="address">4816 Ardmore Rd.<br>Victoria B.C. V8N 4K7</p>
  <div class="divider"></div>
  <ul class="contacts">
    <li><svg viewBox="0 0 14 14"><circle cx="7" cy="7" r="7" fill="var(--brand-green)"/><path d="M4.5,3.5 l1.5,0 .6,2 -1,.7 a5,5 0 0 0 2.2,2.2 l.7,-1 2,.6 0,1.5 c-3.5,.5 -6.5,-2.5 -6,-6z" fill="#fff"/></svg>250-384-6252</li>
    <li><svg viewBox="0 0 14 14"><circle cx="7" cy="7" r="7" fill="var(--brand-green)"/><rect x="5" y="3" width="4" height="8" rx="1" fill="#fff"/></svg>222-222-2222</li>
    <li><svg viewBox="0 0 14 14"><circle cx="7" cy="7" r="7" fill="var(--brand-green)"/><rect x="3.5" y="4.5" width="7" height="5" fill="#fff"/><path d="M3.5,4.5 7,7.5 10.5,4.5" fill="none" stroke="var(--brand-green)" stroke-width="0.8"/></svg>dalton@silverbrookconstructions.example</li>
    <li><svg viewBox="0 0 14 14"><circle cx="7" cy="7" r="7" fill="var(--brand-green)"/><circle cx="7" cy="7" r="3.6" fill="none" stroke="#fff" stroke-width="1"/><path d="M3.4,7 H10.6 M7,3.4 V10.6" stroke="#fff" stroke-width="0.8"/></svg>www.silverbrookconstructions.example</li>
  </ul>
</section>

<section class="card card--front" aria-label="Business card front">
  <svg class="card__edges" viewBox="0 0 540 309" aria-hidden="true">
    <path d="M0,0 H70 C35,70 14,170 0,260 Z" fill="var(--ink-black)"/>
    <path d="M88,-4 C48,70 22,170 12,315" fill="none" stroke="var(--brand-green)" stroke-width="7"/>
  </svg>
  <div class="brand">
    <div class="brand__dot"></div>
    <p class="brand__name">Silver Brook<br>Constructions Ltd</p>
  </div>
</section>

</body>
</html>
```